Business Card for Kinesiologist Practitioner

I need a logo and business card designing for a Kinesiologist Practitioner. I would like the card to be double sided. The look and feel of the logo and graphics should depict natural healing and well being. I would like a modern, fresh and contemporary design with a professional style. I have attached some logos and business cards that I liek from other natural health practitioners. I have also attached some logos that I like and a mock up of the business card style. Please however use your own creative input to change any element as you feel appropriate.

I have used the strap line "Quiet Meadow Care" which I would like underneath the logo. For the logo I like natural objects and possibly with 3 elements in the design as the course I have studied follows a "Lumora " healing concept (mind, body, soul). Maybe a tree or flower with 3 elements and a representation or suggestion of the human body somehow. You will see from the logos i have uploaded

Industry/Entity Type

Business

Contact Information for Business Card

Please see the mock up attached.

Font styles to use
Serif
Sans Serif

Colors
faa54b
acd036
fbee3d
85cae6

Requirements
Must have
• Note the colours are just suggested colours. Please us your own creative licence.

```html
<!DOCTYPE html>
<html lang="en">
<head>
<meta charset="utf-8">
<title>Quiet Meadow Care – Business Card</title>
<link href="https://fonts.googleapis.com/css2?family=Open+Sans:wght@400;600&display=swap" rel="stylesheet">
<style>
  :root {
    --page-bg: #e9ecea;
    --card-white: #ffffff;
    --leaf-green: #9cc41f;
    --leaf-green-light: #b3d83a;
    --leaf-green-dark: #86ad14;
    --sky-blue: #1e9be0;
    --ink: #2b2b2b;
  }
  * { box-sizing: border-box; margin: 0; padding: 0; }
  html, body {
    width: 1200px; height: 900px; overflow: hidden;
    background: var(--page-bg);
    font-family: "Open Sans", Arial, sans-serif;
  }
  .canvas {
    position: relative; width: 1200px; height: 900px;
    display: flex; flex-direction: column; align-items: center;
    justify-content: center; gap: 48px;
  }
  .card {
    position: relative; width: 640px; height: 366px;
    background: var(--card-white);
    box-shadow: 0 6px 18px rgba(0,0,0,0.18);
    overflow: hidden;
  }

  /* Back side */
  .card-back .brand-dot {
    position: absolute; left: 60px; top: 70px;
    width: 200px; height: 200px; border-radius: 50%;
    background: var(--leaf-green-light); opacity: 0.85;
  }
  .card-back .brand-name {
    position: absolute; right: 44px; top: 188px;
    font-size: 30px; font-weight: 400; color: var(--leaf-green);
    white-space: nowrap;
  }

  /* Front side */
  .card-front .brand {
    position: absolute; left: 0; right: 0; top: 34px;
    display: flex; flex-direction: column; align-items: center; gap: 12px;
  }
  .card-front .brand-dot {
    width: 64px; height: 64px; border-radius: 50%;
    background: var(--leaf-green-light); opacity: 0.85;
  }
  .card-front .brand-name {
    font-size: 26px; font-weight: 400; color: var(--leaf-green);
    line-height: 1.1; white-space: nowrap;
  }
  .name-band {
    position: absolute; left: 0; right: 0; top: 152px; height: 62px;
    background: linear-gradient(180deg, var(--leaf-green-light), var(--leaf-green));
    border-top: 3px solid var(--sky-blue);
    border-bottom: 3px solid var(--sky-blue);
    display: flex; align-items: center; justify-content: center; gap: 38px;
    color: var(--card-white);
  }
  .person-name { font-size: 19px; font-weight: 600; }
  .dash { font-size: 18px; }
  .person-role { font-size: 16px; font-weight: 400; }
  .contacts {
    position: absolute; left: 30px; top: 232px;
    list-style: none; display: flex; flex-direction: column; gap: 10px;
  }
  .contact {
    display: flex; align-items: center; gap: 18px;
    font-size: 19px; color: var(--ink);
  }
  .contact-icon {
    width: 22px; height: 22px; border-radius: 4px;
    background: var(--leaf-green); display: flex;
    align-items: center; justify-content: center;
  }
  .footer-band {
    position: absolute; left: 0; right: 0; bottom: 0; height: 40px;
    background: linear-gradient(180deg, var(--leaf-green-light), var(--leaf-green-dark));
  }
</style>
</head>
<body>
<main class="canvas">
  <section class="card card-back" aria-label="Card back">
    <div class="brand-dot"></div>
    <p class="brand-name">Quiet Meadow Care</p>
  </section>

  <section class="card card-front" aria-label="Card front">
    <div class="brand">
      <span class="brand-dot"></span>
      <span class="brand-name">Quiet Meadow Care</span>
    </div>
    <div class="name-band">
      <span class="person-name">Clara Denholm</span>
      <span class="dash">–</span>
      <span class="person-role">Kinesiologist</span>
    </div>
    <ul class="contacts">
      <li class="contact">
        <span class="contact-icon">
          <svg width="14" height="14" viewBox="0 0 24 24" aria-hidden="true">
            <path fill="#fff" d="M6.6 10.8a15.1 15.1 0 0 0 6.6 6.6l2.2-2.2a1 1 0 0 1 1-.25 11.4 11.4 0 0 0 3.6.57 1 1 0 0 1 1 1V20a1 1 0 0 1-1 1A17 17 0 0 1 3 4a1 1 0 0 1 1-1h3.5a1 1 0 0 1 1 1c0 1.25.2 2.45.57 3.6a1 1 0 0 1-.25 1z"/>
          </svg>
        </span>
        <span>0400 555 182</span>
      </li>
      <li class="contact">
        <span class="contact-icon">
          <svg width="16" height="16" viewBox="0 0 24 24" aria-hidden="true">
            <text x="12" y="18" text-anchor="middle" font-family="Open Sans, Arial, sans-serif" font-size="20" font-weight="600" fill="#fff">@</text>
          </svg>
        </span>
        <span>claradenholm@example.com</span>
      </li>
    </ul>
    <div class="footer-band"></div>
  </section>
</main>
</body>
</html>
```